Tide Harbor Finance Business Cards

Looking for a business card for a new mortgage broking business. Name of the business is Tide Harbor Finance. Purpose of the business is to build trust and strong relationships with clients to then assist them with your mortgage lending needs. Most relationships within the business start off as an enquiry, and then can evolve into a 10+ year relationship, servicing clients from purchasing a new home to then upgrading for their family and even then assisting their children with their first home purchase. Business card should communicate financial security and trust.

Target Market(s)

Targeting professional clients who are looking to build a relationship with a knowledgeable mortgage professional

Industry/Entity Type

Finance - Home Loans

Contact Information for Business Card

Peter Colburn, Director, mobile: 0427 903186, email:peter@tideharborfinance.com.au, website: www.tideharborfinance.com.au

Font styles to use
Sans Serif

Requirements
Must have
• On the front: Must have company logo, contact details as above. On the back: slogan, 'full of choices, free of stress', plus listing services offered: home loans, investment loans, first home buyers, refinancing, car finance

```html
<!DOCTYPE html>
<html lang="en">
<head>
<meta charset="utf-8">
<title>Tide Harbor Finance Business Cards</title>
<link rel="stylesheet" href="https://fonts.googleapis.com/css2?family=Montserrat:wght@400;500;700&display=swap">
<style>
  :root {
    --navy: #0f5580;
    --navy-deep: #0b4a72;
    --gold: #f0a21e;
    --white: #ffffff;
    --ink: #1f2b36;
    --stage: #e9ebee;
  }
  * { box-sizing: border-box; margin: 0; padding: 0; }
  html, body { width: 1200px; height: 786px; overflow: hidden; }
  body {
    background: var(--stage);
    font-family: "Montserrat", Arial, sans-serif;
    position: relative;
  }
  .card {
    position: absolute;
    top: 238px;
    width: 530px;
    height: 302px;
    border-bottom: 5px solid var(--gold);
    box-shadow: 0 10px 24px rgba(0,0,0,.18);
    overflow: hidden;
  }
  /* Front */
  .card-front { left: 40px; background: var(--white); }
  .brand-front {
    position: absolute;
    left: 34px;
    top: 84px;
    width: 190px;
    display: flex;
    align-items: center;
    gap: 10px;
  }
  .brand-mark { width: 16px; height: 16px; background: var(--gold); flex: none; }
  .brand-name {
    color: var(--navy);
    font-weight: 700;
    font-size: 23px;
    line-height: 1.08;
    text-transform: uppercase;
    letter-spacing: .5px;
  }
  .divider {
    position: absolute;
    left: 236px;
    top: 52px;
    width: 2px;
    height: 140px;
    background: var(--navy);
  }
  .details { position: absolute; left: 258px; top: 52px; }
  .person-name { color: var(--navy); font-weight: 700; font-size: 22px; }
  .person-role { color: var(--ink); font-size: 12px; margin: 2px 0 14px 2px; }
  .contact-list { list-style: none; }
  .contact-list li {
    display: flex;
    align-items: center;
    gap: 8px;
    font-size: 11.5px;
    color: var(--ink);
    margin-bottom: 7px;
  }
  .contact-list svg { width: 12px; height: 12px; flex: none; }
  .services-band {
    position: absolute;
    left: 0; right: 0; bottom: 7px;
    height: 32px;
    padding: 0 14px;
    background: var(--navy);
    color: var(--white);
    font-size: 10.5px;
    white-space: nowrap;
    display: flex;
    align-items: center;
    justify-content: center;
    gap: 5px;
  }
  .services-band .dot { width: 4px; height: 4px; border-radius: 50%; background: var(--white); flex: none; }
  /* Back */
  .card-back {
    left: 630px;
    background: linear-gradient(135deg, var(--navy) 0%, var(--navy-deep) 100%);
  }
  .brand-back {
    position: absolute;
    left: 0; right: 0;
    top: 92px;
    text-align: center;
  }
  .brand-back .brand-name {
    color: var(--white);
    font-size: 40px;
    line-height: 1.05;
  }
  .slogan {
    position: absolute;
    left: 0; right: 0;
    top: 214px;
    text-align: center;
    color: var(--white);
    font-size: 12px;
    letter-spacing: .4px;
  }
</style>
</head>
<body>
  <section class="card card-front">
    <div class="brand-front">
      <span class="brand-mark"></span>
      <span class="brand-name">Tide Harbor Finance</span>
    </div>
    <div class="divider"></div>
    <div class="details">
      <p class="person-name">Peter Colburn</p>
      <p class="person-role">Director</p>
      <ul class="contact-list">
        <li>
          <svg viewBox="0 0 12 12"><rect x="3" y="0.5" width="6" height="11" rx="1.2" fill="none" stroke="#f0a21e" stroke-width="1.4"/><circle cx="6" cy="9.5" r=".8" fill="#f0a21e"/></svg>
          0427 903186
        </li>
        <li>
          <svg viewBox="0 0 12 12"><rect x="0.5" y="2" width="11" height="8" fill="#0f5580"/><path d="M0.8 2.4 6 6.6 11.2 2.4" fill="none" stroke="#fff" stroke-width="1"/></svg>
          peter@tideharborfinance.com.au
        </li>
        <li>
          <svg viewBox="0 0 12 12"><circle cx="6" cy="6" r="5.3" fill="#0f5580"/><path d="M0.8 6h10.4M6 .8c-2.4 2.8-2.4 7.6 0 10.4M6 .8c2.4 2.8 2.4 7.6 0 10.4" fill="none" stroke="#fff" stroke-width=".8"/></svg>
          www.tideharborfinance.com.au
        </li>
      </ul>
    </div>
    <div class="services-band">
      <span>home loans</span><span class="dot"></span>
      <span>investment loans</span><span class="dot"></span>
      <span>first home buyers</span><span class="dot"></span>
      <span>refinancing</span><span class="dot"></span>
      <span>car finance</span>
    </div>
  </section>

  <section class="card card-back">
    <div class="brand-back">
      <p class="brand-name">Tide Harbor<br>Finance</p>
    </div>
    <p class="slogan">full of choices, free of stress</p>
  </section>
</body>
</html>
```